Clinic information system needs a brochure design with KORV logo

We need to re-design our brochure which is currently with 'Pelix' logo to new 'KORV' logo design. We are a subsidiary company of a Japanese healthcare IT service provider.
Our parent company recently purchased a company called KORV, a traditional drug information service provider, and we will be integrated to this company soon. Thus, we need to update our brochure with the KORV logo.
The vision of our business is to build wide network of healthcare professionals in Asia and to service these customers to improve quality of their work and expand their business.
We provide a cloud-based workflow system and clinic management solutions to our customer clinics. Our mission is to provide information platform, operation system and management tool for healthcare professionals of small and medium medical institutions in Asia enabling them to..
- Build better relationship with patients
- Improve efficiency of medical operation and optimize decision making
- Sustainably grow business
- Contribute to local community
We'd like to see the new brochure which aligns with the newly acquired company, KORV. The look and feel should follow that of KORV which the corporate colour is read. While we comply with the corporate brand, we also want to have uniqueness as our business is totally different from the existing KORV business.
See below links for KORV' websites.
www.korv-example.com
news.korv-example.com
I have attached our current brochure (with old 'Pelix' design). Please refer to this brochure for the contents that needs to be included.
I have also attached the new KORV logo. Please use this for the new brochure.
Target Market(s)
Small and medium size clinics in Philippines and Indonesia
Industry/Entity Type
Clinic
Font styles to use
Other font styles liked:
- I like fonts such as Lato-Light, Century Gothic, Myriad Pro
Look and feel
Each slider illustrates characteristics of the customer's brand and the style your logo design should communicate.

```html
<!DOCTYPE html>
<html lang="en">
<head>
<meta charset="utf-8">
<title>CIS Clinic Information System – KORV Brochure</title>
<link rel="stylesheet" href="https://fonts.googleapis.com/css2?family=Roboto:wght@300;400;500;700&display=swap">
<style>
  :root {
    --brand-red: #c8161d;
    --ink: #2b2b2b;
    --ink-soft: #4a4a4a;
    --paper: #ffffff;
    --cream: #fbf5f1;
    --card: #f1f1f1;
    --photo-light: #d9d6cf;
    --photo-dark: #8e8a80;
  }
  * { margin: 0; padding: 0; box-sizing: border-box; }
  html, body { width: 1200px; height: 808px; overflow: hidden; background: var(--paper); }
  body { font-family: "Roboto", Arial, sans-serif; color: var(--ink); }

  .brochure { position: relative; width: 1200px; height: 808px; }

  .panel { position: absolute; top: 0; height: 808px; }
  .panel--features { left: 0; width: 404px; background: var(--paper); }
  .panel--cover { left: 404px; width: 392px; background: var(--cream); border-left: 1px solid #e6d9d2; border-right: 1px solid #e6d9d2; }
  .panel--modules { left: 796px; width: 404px; background: var(--paper); }

  .title { position: absolute; font-weight: 500; font-size: 40px; line-height: 1; letter-spacing: -0.5px; color: var(--ink); }
  .subtitle { position: absolute; font-weight: 300; font-size: 19px; line-height: 1.2; color: var(--ink); }

  /* Feature list */
  .feature { position: absolute; left: 47px; width: 346px; }
  .feature__num { position: absolute; left: 0; top: 2px; font-weight: 300; font-size: 29px; line-height: 1;
    color: var(--ink); transform: scaleX(0.7); transform-origin: left top; }
  .feature__head { margin-left: 19px; font-weight: 500; font-size: 13.6px; line-height: 17px; color: var(--ink); }
  .feature__head--just { text-align: justify; text-align-last: left; }
  .feature__body { margin-left: 19px; font-weight: 400; font-size: 10.2px; line-height: 13.3px; color: var(--ink-soft); }

  /* Cover */
  .cover__red { position: absolute; left: 0; top: 0; width: 392px; height: 698px; background: var(--brand-red); }
  .cover__photo { position: absolute; left: 0; top: 232px; width: 392px; height: 216px;
    background: linear-gradient(160deg, var(--photo-light) 0%, #bfbab0 55%, var(--photo-dark) 100%); }
  .name-card { position: absolute; left: 42px; top: 294px; width: 308px; height: 86px; background: var(--card);
    border-radius: 16px; display: flex; align-items: center; justify-content: center; }
  .name-card__name { font-weight: 500; font-size: 32px; color: var(--ink); letter-spacing: 1px; }
  .cover__claim { position: absolute; left: 66px; top: 714px; font-weight: 400; font-size: 16px; line-height: 19.6px; color: var(--ink-soft); }

  /* Modules */
  .intro { position: absolute; left: 41px; top: 130px; width: 302px; font-weight: 300; font-size: 13.6px; line-height: 16.6px; color: var(--ink); }
  .intro strong { font-weight: 500; }
  .module { position: absolute; left: 41px; width: 300px; }
  .module__head { font-weight: 500; font-size: 13.6px; line-height: 16.6px; color: var(--ink); }
  .module__body { font-weight: 300; font-size: 13.6px; line-height: 16.6px; color: var(--ink); }
  .module__body--just { text-align: justify; }
</style>
</head>
<body>
<main class="brochure">

  <section class="panel panel--features">
    <h1 class="title" style="left:48px; top:37px;">CIS</h1>
    <p class="subtitle" style="left:47px; top:79px;">Clinic Information System</p>

    <article class="feature" style="top:131px;">
      <span class="feature__num">1</span>
      <h2 class="feature__head feature__head--just">Comprehensive, End–to–End Clinic Workflow Management</h2>
      <p class="feature__body">A revolutionary solution with end–to–end features for simplifying clinic management.<br>Access to the right information, and the automation of complex tasks and workflows is the key focus of CIS, enabling staff to spend more time on caring for patients.</p>
    </article>

    <article class="feature" style="top:250px;">
      <span class="feature__num">2</span>
      <h2 class="feature__head">Access Anywhere, Any Time from Any Device</h2>
      <p class="feature__body">Clinical data is stored in a centralized database on cloud allowing you to access the data whether in the office, an exam room, or at home.<br>Use any laptop, desktop PC, smart phone or tablet to access the system.<br>Runs on all standard web browsers, no need to install any software.</p>
    </article>

    <article class="feature" style="top:360px;">
      <span class="feature__num">3</span>
      <h2 class="feature__head feature__head--just">Flexibility to Meet Different Needs and Priorities of Clinics</h2>
      <p class="feature__body">Prefer to scribble instead of typing on computers? No need for online booking? You can only select the functions you want to use and run the clinic operation in hybrid.<br>Enable to gradually adopt to systemization of the clinic operation by adding functions whenever required and ready in the future.</p>
    </article>

    <article class="feature" style="top:474px;">
      <span class="feature__num">4</span>
      <h2 class="feature__head">Affordable Costs, Easy to Start and Operate</h2>
      <p class="feature__body">Starting from $9.90 per month for a clinic site, no limits to the number of doctors.<br>Offers free trial period for the first three months.<br>Our call center personnel will help you with the initial set–up and answer your questions during use.</p>
    </article>

    <article class="feature" style="top:572px;">
      <span class="feature__num">5</span>
      <h2 class="feature__head">Standards and Regulations Compliant</h2>
      <p class="feature__body">Comply to global medical standards such as HL7, ICD10<br>and Snomed, allowing you to share clinical data across other hospitals and clinics and interface with other surrounding systems, such as PAC system.</p>
    </article>

    <article class="feature" style="top:656px;">
      <span class="feature__num">6</span>
      <h2 class="feature__head">Cloud Based</h2>
      <p class="feature__body">No need to purchase server hardware.<br>Internet connection is sufficient to run the clinic operations.<br>A simple wifi connection is all what is needed.<br>Fully backed–up infrastructure—no worry if any disaster strikes—as all data is in the cloud.<br>Fully available with SSL (secure socket layer) for maximum security.</p>
    </article>
  </section>

  <section class="panel panel--cover">
    <div class="cover__red" role="img" aria-label="Brand red background with large cream organic shapes"></div>
    <div class="cover__photo" role="img" aria-label="Photograph of a bright modern clinic lobby with skylights and plants"></div>
    <div class="name-card">
      <span class="name-card__name">KORV</span>
    </div>
    <p class="cover__claim">A revolutionary solution<br>with end–to–end features<br>for simplifying clinic management</p>
  </section>

  <section class="panel panel--modules">
    <h1 class="title" style="left:41px; top:41px;">CIS</h1>
    <p class="subtitle" style="left:41px; top:83px;">Clinic Information System</p>

    <p class="intro"><strong>CIS</strong> is divided into 6 Core modules and multiple sub–modules. The system is designed with the Patient in central focus.<br>This is to ensure the system assists the users to provide the best in health care practice providing quick information, at all times.</p>

    <div class="module" style="top:246px;">
      <h2 class="module__head">Patient Management</h2>
      <p class="module__body">Covers appointment scheduling<br>and patient registration.</p>
    </div>
    <div class="module" style="top:312px;">
      <h2 class="module__head">Clinic Practice</h2>
      <p class="module__body module__body--just">Essential doctor and nurse sub–modules which include obtaining the patient’s Vitals, Summary of the Encounter, etc.</p>
    </div>
    <div class="module" style="top:395px;">
      <h2 class="module__head">Procedure Services</h2>
      <p class="module__body">Related to doctor’s laboratory requests.</p>
    </div>
    <div class="module" style="top:445px;">
      <h2 class="module__head">Cashier and Billing</h2>
      <p class="module__body">Essential cashiering sub–module which includes Charges Entry, Billing and Payment.</p>
    </div>
    <div class="module" style="top:512px;">
      <h2 class="module__head">Inventory Management</h2>
      <p class="module__body module__body--just">Includes Stock Management and handles transactions of drugs.</p>
    </div>
    <div class="module" style="top:578px;">
      <h2 class="module__head">Patient’s Summary</h2>
      <p class="module__body">Primary patient medical information handling such as Patient Demographics, Allergies, Medical Issues, Trend of Patient’s Vitals, etc.</p>
    </div>
  </section>

</main>
</body>
</html>
```